Chiropractic healthcare group business card

We are a Portland Oregon based chiropractic healthcare group. Looking for a new business card design. Something cutting edge, that shows off our new logo and tag line.Use either of the attached logos.Our tag line = "Who would you be without pain?"I'm open to about anything, impress me!!
Target Market(s)
Chiropractic patients - Auto injury, back pain, sports injuries, neck , shoulder, hip, knee, ankle pain.
Industry/Entity Type
Chiropractic
Contact Information for Business Card
Dr. Bram Holtvick, D.C.
Clinic name - Fernway Chiropractic
2 clinics
location #1
20418 NW Marwick Road
Suite B
North Plains, OR 97133
Location #2
13529 SE Calloway Street
Portland OR 97236
Main phone line 971.555.0143
website : www.FernwayClinics.example
Tag line "Who would you be without pain?"
Colors
Designer to choose colors to be used in the design.
Requirements
Must have
- Use the logo colors -- Want the orange color to be a TRUE orange.
- Both clinic address
- phone number
- website
- personal email - b.holtvick@ReliefBeginsHere.example
- tag line - "Who would you be without pain?"

```html
<!DOCTYPE html>
<html lang="en">
<head>
<meta charset="utf-8">
<title>Fernway Chiropractic – Business Card</title>
<link href="https://fonts.googleapis.com/css2?family=Lora:wght@700&family=Dosis:wght@500;700&display=swap" rel="stylesheet">
<style>
  :root {
    --cream: #fcf8e6;
    --orange: #f5a42c;
    --white: #ffffff;
    --grey: #6b6b6b;
    --ink: #262626;
  }
  html, body {
    margin: 0;
    padding: 0;
    width: 1200px;
    height: 707px;
    overflow: hidden;
    background: var(--cream);
  }
  .card {
    position: relative;
    width: 1200px;
    height: 707px;
    background: var(--cream);
    overflow: hidden;
  }
  .accent-band {
    position: absolute;
    top: 0;
    right: 0;
    width: 227px;
    height: 707px;
    background: var(--orange);
  }
  .brand-block {
    position: absolute;
    left: 72px;
    top: 252px;
  }
  .brand-name {
    margin: 0;
    font-family: "Lora", Georgia, serif;
    font-weight: 700;
    font-size: 67px;
    line-height: 79px;
    letter-spacing: 6px;
    color: var(--orange);
    text-transform: uppercase;
  }
  .brand-name span { display: block; }
  .tagline {
    margin: 14px 0 0 2px;
    font-family: "Dosis", Arial, sans-serif;
    font-weight: 500;
    font-size: 21px;
    letter-spacing: 4px;
    color: var(--grey);
    text-transform: uppercase;
  }
  .contact {
    position: absolute;
    left: 74px;
    top: 566px;
    display: flex;
    gap: 34px;
    font-family: "Dosis", Arial, sans-serif;
    font-weight: 500;
    font-size: 16px;
    line-height: 23px;
    letter-spacing: 0.5px;
    color: var(--grey);
  }
  .contact p { margin: 0; }
  .contact .label {
    font-weight: 700;
    color: var(--orange);
    letter-spacing: 1.5px;
    text-transform: uppercase;
  }
  .emblem {
    position: absolute;
    left: 786px;
    top: 168px;
    width: 370px;
    height: 370px;
  }
  .emblem-name {
    position: absolute;
    left: 786px;
    top: 168px;
    width: 370px;
    height: 370px;
    display: flex;
    flex-direction: column;
    align-items: center;
    justify-content: center;
    font-family: "Lora", Georgia, serif;
    font-weight: 700;
    color: var(--ink);
    text-transform: uppercase;
    text-align: center;
  }
  .emblem-name .main { font-size: 48px; letter-spacing: 8px; line-height: 1; }
  .emblem-name .sub { font-size: 22px; letter-spacing: 3px; margin-top: 8px; line-height: 1; }
</style>
</head>
<body>
  <main class="card">
    <div class="accent-band"></div>

    <section class="brand-block">
      <h1 class="brand-name"><span>Fernway</span><span>Chiropractic</span></h1>
      <p class="tagline">”Who would you be without pain?”</p>
    </section>

    <address class="contact">
      <div class="contact-person">
        <p class="label">Dr. Bram Holtvick, D.C.</p>
        <p>971.555.0143</p>
        <p>www.FernwayClinics.example</p>
        <p>b.holtvick@ReliefBeginsHere.example</p>
      </div>
      <div class="contact-clinic">
        <p class="label">Location 1</p>
        <p>20418 NW Marwick Road</p>
        <p>Suite B</p>
        <p>North Plains, OR 97133</p>
      </div>
      <div class="contact-clinic">
        <p class="label">Location 2</p>
        <p>13529 SE Calloway Street</p>
        <p>Portland, OR 97236</p>
      </div>
    </address>

    <svg class="emblem" viewBox="0 0 370 370" aria-hidden="true">
      <circle cx="185" cy="185" r="185" fill="var(--orange)"/>
      <circle cx="185" cy="185" r="166" fill="var(--white)"/>
    </svg>
    <div class="emblem-name">
      <span class="main">Fernway</span>
      <span class="sub">Chiropractic</span>
    </div>
  </main>
</body>
</html>
```